Solar company mail box flyer design

We are a solar installation company and we currently need a DL flyer design for mailbox distribution. The front page need to mention that the government rebate is going to be reduced from the first day of the next year. Also, it need to mentioned that $100 discount available for any customer who show us this flyer. We will also need to have some solar panels and inverters demonstrated on the front page.

I have attached some similar flyers for reference purpose.

```html
<!DOCTYPE html>
<html lang="en">
<head>
<meta charset="utf-8">
<title>Solar Mailbox Flyer – DL Front</title>
<link href="https://fonts.googleapis.com/css2?family=Oswald:wght@600;700&display=swap" rel="stylesheet">
<style>
  :root {
    --stage-dark: #1c1c1c;
    --stage-light: #6b6b6b;
    --leaf-green: #4f9a1c;
    --leaf-green-light: #7cc231;
    --sun-orange: #f7a000;
    --ink: #0d0d0d;
    --paper: #f4f4f4;
    --paper-shade: #dcdcdc;
    --footer-dark: #262626;
    --sky: #b9d4ea;
    --hill: #5f8f3a;
    --panel-navy: #2b3a78;
    --unit-blue: #2c4f93;
    --unit-red: #d0242a;
    --unit-grey: #e3e3e3;
    --white: #ffffff;
  }
  * { margin: 0; padding: 0; box-sizing: border-box; }
  html, body {
    width: 1200px; height: 1030px; overflow: hidden;
  }
  body {
    background: radial-gradient(ellipse at 50% 50%, var(--stage-light) 0%, var(--stage-dark) 75%);
    font-family: "Oswald", "Arial Narrow", sans-serif;
  }
  .flyer {
    position: absolute; left: 380px; top: 25px;
    width: 440px; height: 980px; overflow: hidden;
    background: var(--paper);
    box-shadow: 0 18px 40px rgba(0,0,0,.55);
  }
  .flyer-shapes { position: absolute; inset: 0; }
  .hero-photo {
    position: absolute; left: 0; top: 0; width: 440px; height: 470px;
    background: linear-gradient(180deg, var(--sky) 0%, #dfe9f2 28%, var(--hill) 48%, #8fb7d9 62%, #4d5f96 100%);
  }
  .brand-name {
    position: absolute; right: 26px; top: 30px;
    font-size: 36px; font-weight: 700; color: var(--sun-orange);
    letter-spacing: .2px;
  }
  .rebate-headline {
    position: absolute; left: 30px; right: 30px; top: 435px;
    text-align: center; color: var(--white);
    font-size: 33px; font-weight: 700; line-height: 1.35;
  }
  .rebate-headline .date { font-size: 40px; }
  .discount-title {
    position: absolute; left: 0; right: 0; top: 640px;
    text-align: center; color: var(--ink);
    font-size: 36px; font-weight: 700;
  }
  .product-row {
    position: absolute; left: 24px; right: 24px; top: 720px; height: 150px;
  }
  .product { position: absolute; }
  .product-panel {
    left: 18px; top: 12px; width: 60px; height: 135px;
    background: linear-gradient(135deg, var(--panel-navy), #1a2456);
    border: 2px solid #c8c8c8;
  }
  .product-inverter {
    left: 100px; top: 0; width: 100px; height: 125px; border-radius: 16px;
    background: linear-gradient(180deg, var(--white), #e6e6e6);
    box-shadow: 0 4px 10px rgba(0,0,0,.15);
  }
  .product-battery-set { left: 216px; top: 0; width: 180px; height: 125px; }
  .battery-cabinet {
    position: absolute; right: 0; top: 0; width: 130px; height: 100px;
    background: var(--unit-grey); border: 1px solid #c9c9c9;
  }
  .battery-blue {
    position: absolute; left: 0; top: 48px; width: 70px; height: 72px;
    background: var(--unit-blue); border-radius: 4px;
  }
  .battery-red {
    position: absolute; left: 62px; top: 64px; width: 44px; height: 44px;
    background: var(--unit-red); border-radius: 4px;
  }
  .website-pill {
    position: absolute; left: 40px; right: 40px; top: 880px; height: 54px;
    border-radius: 27px; background: var(--sun-orange);
    color: var(--white); text-align: center;
    font-size: 34px; font-weight: 700; line-height: 52px;
  }
</style>
</head>
<body>
  <main class="flyer">
    <div class="hero-photo" role="img" aria-label="Photo of wind turbines and ground-mounted solar panels in a green mountain valley"></div>

    <svg class="flyer-shapes" viewBox="0 0 440 980" aria-hidden="true">
      <defs>
        <linearGradient id="greenBand" x1="0" y1="0" x2="1" y2="1">
          <stop offset="0" stop-color="var(--leaf-green-light)"/>
          <stop offset="1" stop-color="var(--leaf-green)"/>
        </linearGradient>
        <linearGradient id="paperFade" x1="0" y1="0" x2="0" y2="1">
          <stop offset="0" stop-color="var(--white)"/>
          <stop offset="1" stop-color="var(--paper-shade)"/>
        </linearGradient>
      </defs>
      <path d="M0,410 C180,405 360,330 440,195 L440,700 L0,700 Z" fill="var(--sun-orange)"/>
      <path d="M0,425 C190,420 370,345 440,225 L440,700 L0,700 Z" fill="url(#greenBand)"/>
      <path d="M0,615 C150,582 330,580 440,690 L440,940 L0,940 Z" fill="var(--sun-orange)"/>
      <path d="M0,632 C150,600 330,598 440,712 L440,940 L0,940 Z" fill="url(#paperFade)"/>
      <rect x="0" y="935" width="440" height="45" fill="var(--footer-dark)"/>
    </svg>

    <div class="brand-name">Company LOGO</div>

    <h1 class="rebate-headline">Government rebate is<br>going to be reduced<br><span class="date">from 1-1-2018</span></h1>

    <h2 class="discount-title">$100 discount</h2>

    <div class="product-row">
      <div class="product product-panel" role="img" aria-label="Solar panel module"></div>
      <div class="product product-inverter" role="img" aria-label="White wall-mounted solar inverter"></div>
      <div class="product product-battery-set" role="img" aria-label="Inverter and battery storage units">
        <div class="battery-cabinet"></div>
        <div class="battery-blue"></div>
        <div class="battery-red"></div>
      </div>
    </div>

    <div class="website-pill">company website</div>
  </main>
</body>
</html>
```